Business Card for my Photography/Video Business

I would like the card to say Event Photographer and Videographer. I like the Black and Gold look to it as well but open to other options. I don't want it to be super vibrant or colorful. Simple, elegant and professional

```html
<!DOCTYPE html>
<html lang="en">
<head>
<meta charset="utf-8">
<title>Kestrel Studio – Business Card</title>
<link href="https://fonts.googleapis.com/css2?family=Arimo:wght@400;700&display=swap" rel="stylesheet">
<style>
  :root {
    --backdrop: #2c3038;
    --card-black: #0d0d0d;
    --card-black-soft: #161616;
    --gold: #b9a068;
    --gold-deep: #8e7642;
    --gold-text: #c9ab6c;
    --rule: rgba(185, 160, 104, 0.55);
  }
  * { box-sizing: border-box; margin: 0; padding: 0; }
  html, body { width: 1200px; height: 900px; overflow: hidden; }
  body {
    background: var(--backdrop);
    font-family: "Arimo", Arial, sans-serif;
    position: relative;
  }
  .card {
    position: absolute;
    left: 320px;
    width: 560px;
    height: 320px;
    background: var(--card-black);
    overflow: hidden;
  }
  .card--front { top: 95px; }
  .card--back { top: 485px; }

  /* Front */
  .brand-mark {
    position: absolute;
    left: 48px;
    top: 42px;
    width: 170px;
    height: 170px;
    border-radius: 50%;
    background: radial-gradient(circle at 40% 35%, var(--gold), var(--gold-deep));
  }
  .brand-name {
    position: absolute;
    left: 48px;
    top: 226px;
    width: 170px;
    text-align: center;
    color: var(--gold-text);
    font-size: 15px;
    font-weight: 700;
    letter-spacing: 2px;
    text-transform: uppercase;
  }
  .identity {
    position: absolute;
    left: 270px;
    top: 46px;
    width: 260px;
  }
  .identity__name {
    color: var(--gold-text);
    font-size: 21px;
    font-weight: 700;
    letter-spacing: 0.5px;
  }
  .identity__role {
    color: var(--gold-text);
    font-size: 14px;
    margin-top: 4px;
  }
  .contact-list {
    position: absolute;
    left: 270px;
    top: 112px;
    width: 250px;
    list-style: none;
  }
  .contact-row {
    position: relative;
    height: 44px;
    border-top: 1px solid var(--rule);
    display: flex;
    align-items: center;
    gap: 12px;
  }
  .contact-row:last-child { border-bottom: 1px solid var(--rule); }
  .contact-row svg { flex: none; }
  .contact-row span {
    color: var(--gold-text);
    font-size: 14px;
  }
  .accent-band {
    position: absolute;
    left: 0;
    bottom: 0;
    width: 100%;
    height: 12px;
    background: var(--gold);
  }

  /* Back */
  .back-texture {
    position: absolute;
    inset: 0;
    background: radial-gradient(circle at 50% 40%, var(--card-black-soft), var(--card-black));
  }
  .back-web {
    position: absolute;
    left: 36px;
    bottom: 30px;
    color: var(--gold-text);
    font-size: 12px;
  }
  .back-brand {
    position: absolute;
    right: 36px;
    bottom: 26px;
    display: flex;
    align-items: center;
    gap: 10px;
  }
  .back-brand__dot {
    width: 60px;
    height: 60px;
    border-radius: 50%;
    background: radial-gradient(circle at 40% 35%, var(--gold), var(--gold-deep));
  }
  .back-brand__name {
    color: var(--gold-text);
    font-size: 13px;
    font-weight: 700;
    letter-spacing: 1.5px;
    text-transform: uppercase;
  }
</style>
</head>
<body>

<section class="card card--front">
  <div class="brand-mark"></div>
  <div class="brand-name">Kestrel Studio</div>

  <div class="identity">
    <div class="identity__name">DANIEL REYES</div>
    <div class="identity__role">Event Photographer and Videographer</div>
  </div>

  <ul class="contact-list">
    <li class="contact-row">
      <svg width="24" height="24" viewBox="0 0 24 24" aria-hidden="true">
        <circle cx="12" cy="12" r="12" fill="#b9a068"/>
        <path d="M9 6.5l1.8 2.6-1.2 1.3c.7 1.5 1.8 2.6 3.2 3.3l1.3-1.2 2.6 1.7-.8 2c-3.8.2-7.6-3.8-7.7-7.6z" fill="#0d0d0d"/>
      </svg>
      <span>5550 1234 8876</span>
    </li>
    <li class="contact-row">
      <svg width="24" height="24" viewBox="0 0 24 24" aria-hidden="true">
        <circle cx="12" cy="12" r="12" fill="#b9a068"/>
        <rect x="6.5" y="8" width="11" height="8" fill="none" stroke="#0d0d0d" stroke-width="1.4"/>
        <path d="M6.5 8l5.5 4.5L17.5 8" fill="none" stroke="#0d0d0d" stroke-width="1.4"/>
      </svg>
      <span>dan@kestrelstudio.com</span>
    </li>
    <li class="contact-row">
      <svg width="24" height="24" viewBox="0 0 24 24" aria-hidden="true">
        <circle cx="12" cy="12" r="12" fill="#b9a068"/>
        <circle cx="12" cy="12" r="5.5" fill="none" stroke="#0d0d0d" stroke-width="1.3"/>
        <ellipse cx="12" cy="12" rx="2.4" ry="5.5" fill="none" stroke="#0d0d0d" stroke-width="1.1"/>
        <path d="M6.5 12h11M7.5 9.3h9M7.5 14.7h9" stroke="#0d0d0d" stroke-width="1"/>
      </svg>
      <span>www.kestrelstudio.com</span>
    </li>
  </ul>

  <div class="accent-band"></div>
</section>

<section class="card card--back">
  <div class="back-texture" role="img" aria-label="Faint repeating pattern of the studio monogram in dark tones"></div>
  <div class="back-web">www.kestrelstudio.com</div>
  <div class="back-brand">
    <div class="back-brand__dot"></div>
    <div class="back-brand__name">Kestrel Studio</div>
  </div>
</section>

</body>
</html>
```